Environmentally friendly Home and Office cleaning service needs a logo and web design!

Tidewell Housekeeping is a new startup looking for a logo and web design. We're base in Ottawa, Canada, and all of our products are eco-friendly, as well as being easy on the sensitivities of our clients.
We wash windows, walls, kitchens, bathrooms, dust, vacuum and wash floors on our hands and knees, and bring all of our own gear and supplies.
plumrake.example was my last website. It's functional, not bad - but just isn't great. I'm looking for a simple design, with few links or clickable buttons.
Colours I will leave to your creative mind to decide. I just want to see something that is relevant to "Tidewell Housekeeping."

Target Market(s)

Often it's women and gay men, ages 35-70
White collar government workers, usually with pets (cats, dogs)

Industry/Entity Type

Cleaning Service

Logo Text

Tidewell Housekeeping

Number of Pages Required

1 page

Font styles to use
Sans Serif

Colors

Designer to choose colors to be used in the design.

Requirements
Must have
• Colour, pictures

```html
<!DOCTYPE html>
<html lang="en">
<head>
<meta charset="utf-8">
<title>Tidewell Housekeeping</title>
<link rel="stylesheet" href="https://fonts.googleapis.com/css2?family=Raleway:wght@400;500;600;700&family=Roboto:wght@400;500;700&display=swap">
<style>
  :root {
    --green: #58b548;
    --green-soft: #6ab04c;
    --blue: #2f6db5;
    --navy: #0b4a8c;
    --orange: #f07a23;
    --ink: #333333;
    --body: #555555;
    --white: #ffffff;
  }
  * { box-sizing: border-box; margin: 0; padding: 0; }
  html, body { width: 1200px; height: 2740px; overflow: hidden; }
  body { position: relative; background: var(--white); font-family: "Raleway", sans-serif; color: var(--body); }

  /* Hero */
  .hero { position: absolute; left: 0; top: 0; width: 1200px; height: 663px;
    background: linear-gradient(180deg, #e4ecea 0%, #eef3f1 22%, #dfe9e7 40%, #b9d6d3 52%, #a9cbc8 60%, #cfdcdd 64%, #b7c4ca 76%, #98a9b2 88%, #8796a0 100%); }
  .hero-title { position: absolute; left: 0; right: 0; top: 330px; text-align: center;
    font-family: "Roboto", sans-serif; font-weight: 700; font-size: 40px; color: var(--white);
    text-shadow: 0 2px 6px rgba(0,0,0,.55); letter-spacing: .5px; }

  /* Header */
  .site-header { position: absolute; left: 0; top: 0; width: 1200px; height: 115px; background: rgba(92,172,82,.82); }
  .brand { position: absolute; left: 88px; top: 46px; display: flex; align-items: center; gap: 12px;
    font-family: "Raleway", sans-serif; font-weight: 600; font-size: 28px; color: var(--white); }
  .brand-mark { width: 30px; height: 30px; border-radius: 50%; background: var(--white); }
  .social-top { position: absolute; right: 30px; top: 8px; display: flex; gap: 14px; }
  .social-top span { width: 14px; height: 14px; border-radius: 50%; background: var(--white); }
  .header-phone { position: absolute; left: 606px; top: 66px; display: flex; align-items: center; gap: 10px;
    color: var(--white); font-size: 15px; font-weight: 500; }
  .header-search { position: absolute; left: 785px; top: 62px; width: 223px; height: 22px; border-bottom: 1px solid var(--white);
    color: var(--white); font-size: 12px; }
  .header-search svg { position: absolute; right: 2px; top: 2px; }
  .header-menu { position: absolute; left: 1040px; top: 66px; display: flex; align-items: center; gap: 10px;
    color: var(--white); font-size: 14px; }

  /* Service tiles */
  .services { position: absolute; left: 0; top: 663px; width: 1200px; height: 200px; display: flex; }
  .service { width: 200px; height: 200px; color: var(--white); text-align: center; padding-top: 24px; }
  .service.blue { background: var(--blue); clip-path: polygon(0 0,100% 0,100% 155px,0 200px); }
  .service.orange { background: var(--orange); clip-path: polygon(0 0,100% 0,100% 200px,0 155px); }
  .service svg { display: block; margin: 0 auto 10px; }
  .service-name { font-family: "Roboto", sans-serif; font-size: 26px; line-height: 30px; }
  .service-sub { font-size: 20px; line-height: 24px; }

  /* Intro */
  .intro { position: absolute; left: 90px; top: 925px; width: 1020px; text-align: center; }
  .intro h1 { font-family: "Roboto", sans-serif; font-weight: 700; font-size: 29px; color: var(--ink); line-height: 38px; }
  .intro h1 span { display: block; font-weight: 400; color: var(--orange); }
  .divider { position: relative; width: 300px; height: 20px; margin: 16px auto 26px; }
  .divider::before, .divider::after { content: ""; position: absolute; top: 9px; width: 120px; height: 1px; background: var(--blue); }
  .divider::before { left: 0; } .divider::after { right: 0; }
  .divider i { position: absolute; left: 143px; top: 3px; width: 14px; height: 14px; border-radius: 50%; background: var(--orange); }
  .intro p { font-size: 16.5px; line-height: 26px; color: var(--body); margin-bottom: 26px; }

  /* Eco band */
  .eco { position: absolute; left: 0; top: 1351px; width: 1200px; height: 362px;
    background: linear-gradient(90deg, #c4560f 0%, #cf6418 35%, #b9531a 58%, #6a3a22 70%, #2e2522 80%, #4a4446 90%, #7d7a7c 100%); }
  .eco h2 { position: absolute; left: 92px; top: 36px; font-family: "Roboto", sans-serif; font-weight: 500; font-size: 28px; color: var(--white); }
  .eco ul { position: absolute; left: 92px; top: 110px; list-style: none; color: var(--white); font-size: 18px; line-height: 26px; }
  .eco li { position: relative; padding-left: 32px; margin-bottom: 20px; }
  .eco li svg { position: absolute; left: 0; top: 4px; }

  /* How it works */
  .how-photo { position: absolute; left: 0; top: 1716px; width: 599px; height: 588px;
    background: linear-gradient(135deg, #dfe8ee 0%, #eef3f6 30%, #f1e9df 48%, #e9d9b0 58%, #dfe6ea 72%, #b8c3cc 100%); }
  .how-box { position: absolute; left: 447px; top: 1780px; width: 753px; height: 484px; background: var(--green);
    color: var(--white); padding: 30px 90px 0 36px; }
  .how-box h2 { font-family: "Roboto", sans-serif; font-weight: 500; font-size: 30px; line-height: 34px; }
  .how-box h3 { font-family: "Roboto", sans-serif; font-weight: 700; font-size: 20px; line-height: 28px; }
  .how-rule { width: 104px; height: 3px; background: var(--orange); margin: 8px 0 24px; }
  .how-item { position: relative; padding-left: 52px; font-size: 14.5px; line-height: 24px; margin-bottom: 18px; }
  .how-item svg { position: absolute; left: 8px; top: 0; }

  /* About */
  .about { position: absolute; left: 88px; top: 2370px; width: 1024px; }
  .about h2 { font-family: "Roboto", sans-serif; font-weight: 500; font-size: 26px; color: #1e5aa0; margin-bottom: 12px; }
  .about p { font-size: 13px; line-height: 27px; color: var(--ink); }

  /* Footer */
  .site-footer { position: absolute; left: 0; top: 2582px; width: 1200px; height: 111px; background: var(--navy); }
  .pill { position: absolute; top: 33px; height: 46px; border: 1px solid rgba(255,255,255,.7); border-radius: 23px;
    display: flex; align-items: center; justify-content: center; gap: 14px; color: var(--white); font-size: 17px; font-weight: 500; }
  .pill.phone { left: 86px; width: 215px; }
  .pill.email { left: 440px; width: 318px; font-size: 16px; }
  .pill.social { left: 897px; width: 215px; gap: 24px; }
  .pill.social span { width: 16px; height: 16px; border-radius: 50%; background: var(--white); }
  .copyright { position: absolute; left: 0; top: 2693px; width: 1200px; height: 47px; background: var(--green-soft);
    color: #e8f4e2; font-size: 12px; text-align: center; line-height: 47px; }
</style>
</head>
<body>

<section class="hero" role="img" aria-label="Photo of a cleaner mopping a tiled floor beside a cleaning cart and a wet-floor sign">
  <h1 class="hero-title">WELCOME TO TIDEWELL HOUSEKEEPING</h1>
</section>

<header class="site-header">
  <div class="brand"><span class="brand-mark"></span>Tidewell Housekeeping</div>
  <div class="social-top"><span></span><span></span><span></span><span></span></div>
  <div class="header-phone">
    <svg width="22" height="18" viewBox="0 0 22 18"><path d="M2 6c0-3 4-4 9-4s9 1 9 4l-4 2-2-2H8L6 8z" fill="#fff"/><rect x="4" y="9" width="14" height="8" rx="2" fill="#fff"/></svg>
    613-555-0142
  </div>
  <div class="header-search">Search...
    <svg width="12" height="12" viewBox="0 0 12 12"><circle cx="5" cy="5" r="3.5" stroke="#fff" stroke-width="1.6" fill="none"/><line x1="7.5" y1="7.5" x2="11" y2="11" stroke="#fff" stroke-width="1.6"/></svg>
  </div>
  <div class="header-menu">Menu
    <svg width="24" height="18" viewBox="0 0 24 18"><rect y="1" width="24" height="3" fill="#fff"/><rect y="8" width="24" height="3" fill="#fff"/><rect y="15" width="24" height="3" fill="#fff"/></svg>
  </div>
</header>

<nav class="services">
  <div class="service blue">
    <svg width="44" height="52" viewBox="0 0 44 52" fill="none" stroke="#fff" stroke-width="2.4"><path d="M4 50V20a18 18 0 0 1 36 0v30z"/><line x1="22" y1="2" x2="22" y2="50"/><line x1="4" y1="26" x2="40" y2="26"/></svg>
    <div class="service-name">Windows</div><div class="service-sub">Wash</div>
  </div>
  <div class="service orange">
    <svg width="52" height="52" viewBox="0 0 52 52" fill="none" stroke="#fff" stroke-width="2.4"><rect x="22" y="4" width="26" height="14" rx="2" transform="rotate(40 35 11)"/><path d="M24 24 8 44l4 4 18-18"/></svg>
    <div class="service-name">Walls</div><div class="service-sub">Wash</div>
  </div>
  <div class="service blue">
    <svg width="56" height="52" viewBox="0 0 56 52" fill="none" stroke="#fff" stroke-width="2.4"><path d="M12 24V8a5 5 0 0 1 10 0"/><path d="M4 24h48v6a14 14 0 0 1-14 14H18A14 14 0 0 1 4 30z"/><line x1="14" y1="44" x2="12" y2="50"/><line x1="42" y1="44" x2="44" y2="50"/></svg>
    <div class="service-name">Bathrooms</div><div class="service-sub">Wash</div>
  </div>
  <div class="service orange">
    <svg width="56" height="52" viewBox="0 0 56 52" fill="none" stroke="#fff" stroke-width="2.4"><path d="M22 14V6h12v6"/><rect x="4" y="18" width="48" height="26" rx="2"/><line x1="28" y1="18" x2="28" y2="44"/><line x1="10" y1="30" x2="22" y2="30"/><line x1="34" y1="30" x2="46" y2="30"/></svg>
    <div class="service-name">Kitchens</div><div class="service-sub">Wash</div>
  </div>
  <div class="service blue">
    <svg width="52" height="52" viewBox="0 0 52 52" fill="none" stroke="#fff" stroke-width="2.4"><line x1="40" y1="4" x2="26" y2="26"/><path d="M26 26c-10-4-20 6-18 20 8 2 18-4 22-12z"/><path d="M12 44l8-10M18 46l6-8"/></svg>
    <div class="service-name">Dust</div><div class="service-sub">Wash</div>
  </div>
  <div class="service orange">
    <svg width="56" height="52" viewBox="0 0 56 52" fill="none" stroke="#fff" stroke-width="2.4"><path d="M6 40c0-12 10-22 24-22"/><path d="M6 40h30a10 10 0 0 0-10-14"/><circle cx="42" cy="38" r="8"/><line x1="30" y1="18" x2="24" y2="6"/></svg>
    <div class="service-name">Floors</div><div class="service-sub">Wash</div>
  </div>
</nav>

<section class="intro">
  <h1>LET US BE PART OF YOUR TEAM TO KEEP<span>YOUR SPACE CLEAN!</span></h1>
  <div class="divider"><i></i></div>
  <p>We will give your home the respect it deserves with careful attention to detal and thorough work. It can be a relief to know that you can leave and come back and never have to worry about dusting, vacuuming, windows or walls.</p>
  <p>We do all of that for you!<br>You don't even have to think about providing any materials for us since we supply all of our own gear and equipment, all of which is 100% eco-friend and kind on sensitivities.</p>
  <p>We are insured and have references available to confirm our work ethic and trustworthiness.</p>
</section>

<section class="eco" role="img" aria-label="Photo of a gloved hand wiping a dark countertop with a cloth, under an orange tint">
  <h2>What Makes Tidewell Housekeeping Environmentally Friendly?</h2>
  <ul>
    <li><svg width="18" height="18" viewBox="0 0 18 18" fill="none" stroke="#fff" stroke-width="1.5"><circle cx="9" cy="9" r="5"/><path d="M9 0v5M9 13v5M0 9h5M13 9h5"/></svg>We use unscented, non-toxic, chemical-free cleaners</li>
    <li><svg width="18" height="18" viewBox="0 0 18 18" fill="none" stroke="#fff" stroke-width="1.5"><circle cx="9" cy="9" r="5"/><path d="M9 0v5M9 13v5M0 9h5M13 9h5"/></svg>We use vinegar as an antiseptic and deodorizer when needed,<br>as well as for windows and mirrors</li>
    <li><svg width="18" height="18" viewBox="0 0 18 18" fill="none" stroke="#fff" stroke-width="1.5"><circle cx="9" cy="9" r="5"/><path d="M9 0v5M9 13v5M0 9h5M13 9h5"/></svg>We use baking soda if we need more aggressive scrubbing</li>
    <li><svg width="18" height="18" viewBox="0 0 18 18" fill="none" stroke="#fff" stroke-width="1.5"><circle cx="9" cy="9" r="5"/><path d="M9 0v5M9 13v5M0 9h5M13 9h5"/></svg>We use a HEPA-filter vacuum for allergen relief</li>
  </ul>
</section>

<div class="how-photo" role="img" aria-label="Photo of a cleaner in yellow gloves wiping a window with a spray bottle"></div>
<section class="how-box">
  <h2>How it Works</h2>
  <h3>The first clean is half-off because:</h3>
  <div class="how-rule"></div>
  <div class="how-item"><svg width="28" height="22" viewBox="0 0 28 22" fill="none" stroke="#fff" stroke-width="1.6"><path d="M2 10h6l10-8 2 2-6 6h12v3H18M8 10v10h12l2-7"/></svg>We don't give estimates. Houses can be very deceiving, and we &nbsp;don't want to set inappropriate expectations. The discounted rate gives us the ability to estimate just how long regular cleans will take.</div>
  <div class="how-item"><svg width="28" height="22" viewBox="0 0 28 22" fill="none" stroke="#fff" stroke-width="1.6"><path d="M2 10h6l10-8 2 2-6 6h12v3H18M8 10v10h12l2-7"/></svg>This also gives you the chance to test us out and see if we're a good fit.</div>
  <div class="how-item">For the first clean, it'd be ideal if you were there so that we can go room to room and make sure everything is exactly as you like it to be. I don't want us leaving until you're happy!</div>
  <div class="how-item">Assuming you like what you see, we can then schedule regular appointments. I will have a copy of your keys made and initial them so that no one knows who these keys belong to (Jane Doe would be "JD").</div>
</section>

<section class="about">
  <h2>Who Am I?</h2>
  <p>Hi!</p>
  <p>My name is Dana Whitmore and I have been a professional cleaner in the Ottawa area for over 2 years, under the tutelage of Glen Harcourt, another professional with more than 15 years experience in the field. He taught me everything he knows about what clients want from their cleaners: a meticulous eye for detail, reliability and to always search for the difference that makes a difference in the client's eyes.</p>
</section>

<footer class="site-footer">
  <div class="pill phone">
    <svg width="24" height="20" viewBox="0 0 22 18"><path d="M2 6c0-3 4-4 9-4s9 1 9 4l-4 2-2-2H8L6 8z" fill="#fff"/><rect x="4" y="9" width="14" height="8" rx="2" fill="#fff"/></svg>
    613-555-0142
  </div>
  <div class="pill email">
    <svg width="22" height="18" viewBox="0 0 22 18" fill="none" stroke="#fff" stroke-width="1.6"><rect x="1" y="1" width="20" height="16" rx="1"/><path d="M1 2l10 8 10-8"/></svg>
    dana.whitmore@mailbox.example
  </div>
  <div class="pill social"><span></span><span></span><span></span><span></span></div>
</footer>
<div class="copyright">© Copyright 2017 Tidewell Housekeeping | All Rights Reserved.</div>

</body>
</html>
```